Bref créative
Business card and stationary for Maplecrest Vision Studio Eye Clinic
Maplecrest Vision Studio / (Clear Sight Daily)
Professional
Dr. Marcus Pell, O.D.
Optometric Physician
Bayline Office
2864 Larkwood Ave
Tampa, FL. 33629
Emergency:813-555-0487
maplecrestvisionstudiohub@mailbox-demo.net
www.maplecrestvisionstudio-demo.com
Appointment
Date:_______ @ ______ AM / PM
WWW.MAPLECRESTVISIONSTUDIO-DEMO.COM
if unable to keep appointment kindly give 24 hours notice.
I need a business card and brochure made for my office with the new logo.

```html
<!DOCTYPE html>
<html lang="en">
<head>
<meta charset="utf-8">
<title>Maplecrest Vision Studio – Business Card</title>
<link rel="stylesheet" href="https://fonts.googleapis.com/css2?family=Open+Sans:ital,wght@0,400;0,600;1,400&display=swap">
<style>
  :root {
    --bg: #ecebe8;
    --card: #ffffff;
    --ink: #2c3a48;
    --blue: #2b9fd4;
    --grey: #6b7580;
    --rule: #c9ced3;
  }
  * { margin: 0; padding: 0; box-sizing: border-box; }
  html, body { width: 1200px; height: 988px; overflow: hidden; }
  body {
    background: var(--bg);
    font-family: "Open Sans", sans-serif;
    color: var(--ink);
    display: flex;
    flex-direction: column;
    align-items: center;
    justify-content: center;
    gap: 44px;
  }
  .card {
    width: 760px;
    height: 430px;
    background: var(--card);
    box-shadow: 0 4px 18px rgba(0,0,0,0.12);
    position: relative;
  }

  /* back face */
  .card-back { display: flex; align-items: center; justify-content: center; }
  .brand { display: flex; flex-direction: column; align-items: center; }
  .brand-mark { display: flex; align-items: center; gap: 14px; }
  .brand-dot { width: 22px; height: 22px; border-radius: 50%; background: var(--blue); }
  .brand-name {
    font-weight: 600;
    color: var(--ink);
    letter-spacing: 1px;
    text-transform: uppercase;
  }
  .brand-tagline {
    font-style: italic;
    color: var(--blue);
    margin-top: 6px;
  }
  .card-back .brand-name { font-size: 30px; }
  .card-back .brand-tagline { font-size: 18px; }

  /* front face */
  .card-front { display: flex; align-items: center; padding: 0 40px 0 50px; }
  .card-front .brand { width: 380px; align-items: flex-start; }
  .card-front .brand-name { font-size: 26px; line-height: 1.2; }
  .card-front .brand-tagline { font-size: 17px; margin-left: 36px; }
  .divider { width: 1px; height: 230px; background: var(--rule); margin: 0 26px; }
  .contact { flex: 1; }
  .person-name { color: var(--blue); font-weight: 600; font-size: 16px; }
  .person-title { color: var(--grey); font-size: 13px; margin-bottom: 14px; }
  .contact-list { list-style: none; }
  .contact-list li {
    display: flex;
    align-items: flex-start;
    gap: 8px;
    font-size: 11.5px;
    line-height: 1.4;
    color: var(--grey);
    margin-bottom: 5px;
  }
  .contact-icon { flex: none; width: 15px; height: 15px; margin-top: 1px; }
</style>
</head>
<body>

  <section class="card card-back" aria-label="Card back">
    <div class="brand">
      <div class="brand-mark">
        <span class="brand-dot"></span>
        <span class="brand-name">Maplecrest Vision Studio</span>
      </div>
      <p class="brand-tagline">Clear Sight Daily</p>
    </div>
  </section>

  <section class="card card-front" aria-label="Card front">
    <div class="brand">
      <div class="brand-mark">
        <span class="brand-dot"></span>
        <span class="brand-name">Maplecrest Vision Studio</span>
      </div>
      <p class="brand-tagline">Clear Sight Daily</p>
    </div>

    <div class="divider"></div>

    <div class="contact">
      <p class="person-name">Dr. Marcus Pell, O.D.</p>
      <p class="person-title">Optometric Physician</p>
      <ul class="contact-list">
        <li>
          <svg class="contact-icon" viewBox="0 0 16 16"><circle cx="8" cy="8" r="8" fill="#2b9fd4"/><path d="M8 3.5a3 3 0 0 0-3 3c0 2.3 3 6 3 6s3-3.7 3-6a3 3 0 0 0-3-3zm0 4.2a1.2 1.2 0 1 1 0-2.4 1.2 1.2 0 0 1 0 2.4z" fill="#fff"/></svg>
          <span>Bayline Office 2864 Larkwood Ave<br>Tampa, FL 33629</span>
        </li>
        <li>
          <svg class="contact-icon" viewBox="0 0 16 16"><circle cx="8" cy="8" r="8" fill="#2b9fd4"/><path d="M5.4 4.2l1.3-.3.8 2-1 .7a5.5 5.5 0 0 0 2.9 2.9l.7-1 2 .8-.3 1.3c-.1.4-.5.7-.9.6A7.2 7.2 0 0 1 4.8 5.1c-.1-.4.2-.8.6-.9z" fill="#fff"/></svg>
          <span>813-555-0162</span>
        </li>
        <li>
          <svg class="contact-icon" viewBox="0 0 16 16"><circle cx="8" cy="8" r="8" fill="#2b9fd4"/><path d="M5.4 4.2l1.3-.3.8 2-1 .7a5.5 5.5 0 0 0 2.9 2.9l.7-1 2 .8-.3 1.3c-.1.4-.5.7-.9.6A7.2 7.2 0 0 1 4.8 5.1c-.1-.4.2-.8.6-.9z" fill="#fff"/></svg>
          <span>813-555-0487</span>
        </li>
        <li>
          <svg class="contact-icon" viewBox="0 0 16 16"><circle cx="8" cy="8" r="8" fill="#2b9fd4"/><rect x="4.5" y="4" width="7" height="8" rx="1" fill="#fff"/><rect x="6" y="5.5" width="4" height="1" fill="#2b9fd4"/></svg>
          <span>813-555-0219</span>
        </li>
        <li>
          <svg class="contact-icon" viewBox="0 0 16 16"><circle cx="8" cy="8" r="8" fill="#2b9fd4"/><rect x="4" y="5" width="8" height="6" rx="0.8" fill="#fff"/><path d="M4.3 5.4L8 8.3l3.7-2.9" fill="none" stroke="#2b9fd4" stroke-width="0.9"/></svg>
          <span>maplecrestvisionstudiohub@mailbox-demo.net</span>
        </li>
        <li>
          <svg class="contact-icon" viewBox="0 0 16 16"><circle cx="8" cy="8" r="8" fill="#2b9fd4"/><circle cx="8" cy="8" r="3.6" fill="none" stroke="#fff" stroke-width="1"/><path d="M4.4 8h7.2M8 4.4c-1.5 2.2-1.5 5 0 7.2M8 4.4c1.5 2.2 1.5 5 0 7.2" fill="none" stroke="#fff" stroke-width="0.8"/></svg>
          <span>www.maplecrestvisionstudio-demo.com</span>
        </li>
      </ul>
    </div>
  </section>

</body>
</html>
```